Cedar Harbor Business Cards For New Startup

I am looking for you to design some business cards for a new startup https://cedarharborhub.com. I have supplied logo, brand guidelines and our signatures as a guide.

We need this to reflect the brand guidelines and the website for brand consistency,

What is Cedar Harbor?

Mallorca's Business Growth Community
Join your new business community full of passionate entrepreneurs who
love to solve problems and help each other grow together!

Any questions you can ask.

Target Market(s)

Business to Business

Contact Information for Business Card

These are attached (signatures) to the job

Font styles to use
Other font styles liked:
• Open Sans

Requirements
Must have
• Match design guidelines
Nice to have
• Photos of our faces so people remember us

```html
<!DOCTYPE html>
<html lang="en">
<head>
<meta charset="utf-8">
<title>Cedar Harbor Business Cards</title>
<link href="https://fonts.googleapis.com/css2?family=Open+Sans:wght@300;400;600;700&display=swap" rel="stylesheet">
<style>
  :root {
    --bg: #d9d9d6;
    --brown: #654f22;
    --brown-light: #6e5727;
    --brown-shade: #57431c;
    --olive: #636b2c;
    --olive-light: #6b7432;
    --white: #ffffff;
    --photo-a: #efe4d8;
    --photo-b: #d8c29a;
  }
  * { margin: 0; padding: 0; box-sizing: border-box; }
  html, body {
    width: 960px; height: 1200px; overflow: hidden;
    background: var(--bg);
    font-family: "Open Sans", Arial, sans-serif;
  }
  .canvas { position: relative; width: 960px; height: 1200px; }
  .card {
    position: absolute; left: 80px; width: 800px; height: 444px;
    box-shadow: 0 6px 18px rgba(0,0,0,.25);
    overflow: hidden; color: var(--white);
  }
  .card--front { top: 114px; }
  .card--back { top: 642px; }
  .card__art { position: absolute; inset: 0; width: 800px; height: 444px; display: block; }
  .portrait {
    position: absolute; left: 4px; top: 4px; width: 270px; height: 270px;
    background: radial-gradient(circle at 50% 45%, var(--photo-a), var(--photo-b));
  }
  .brand-mark {
    position: absolute; left: 418px; top: 26px; width: 70px; height: 70px;
    border: 3px solid var(--white); border-radius: 50%;
  }
  .brand-name {
    position: absolute; font-weight: 600; letter-spacing: .5px; white-space: nowrap;
  }
  .card--front .brand-name { left: 354px; top: 104px; font-size: 30px; width: 200px; text-align: center; }
  .card__person { position: absolute; left: 0; top: 294px; width: 288px; text-align: center; }
  .person-name { font-weight: 700; font-size: 27px; line-height: 1.2; }
  .person-role { font-weight: 300; font-size: 15px; margin-top: 6px; }
  .card__contact {
    position: absolute; left: 92px; top: 405px; font-size: 25px; font-weight: 600;
    letter-spacing: 3px; white-space: nowrap; display: flex; gap: 48px;
  }
  .badge {
    position: absolute; left: 110px; top: 32px; width: 138px; height: 138px;
    background: var(--olive); border-radius: 12px;
  }
  .card--back .brand-name { left: 42px; top: 180px; font-size: 42px; }
  .card__url {
    position: absolute; right: 20px; top: 400px; font-size: 33px; font-weight: 600;
    letter-spacing: 8px; white-space: nowrap;
  }
</style>
</head>
<body>
<main class="canvas">
  <section class="card card--front" aria-label="Business card front">
    <svg class="card__art" viewBox="0 0 800 444" aria-hidden="true">
      <rect width="800" height="444" fill="var(--brown)"/>
      <rect x="0" y="0" width="322" height="444" fill="var(--olive)"/>
      <polygon points="322,0 370,0 370,320 322,352" fill="var(--olive-light)"/>
      <polygon points="800,0 218,395 382,395" fill="var(--brown-light)"/>
      <polygon points="800,0 382,395 575,395" fill="var(--olive)"/>
      <polygon points="700,156 800,156 800,206 640,206" fill="var(--olive)"/>
      <polygon points="700,206 800,206 800,290 620,290" fill="var(--brown-shade)" opacity=".35"/>
      <polygon points="610,290 800,290 800,340 590,340" fill="var(--olive)"/>
      <polygon points="42,395 800,395 800,444 0,444" fill="var(--olive)"/>
      <polygon points="0,395 42,395 0,444" fill="var(--brown-shade)"/>
    </svg>
    <div class="portrait" role="img" aria-label="Portrait photo of the card holder"></div>
    <div class="brand-mark" aria-hidden="true"></div>
    <div class="brand-name">CEDAR HARBOR</div>
    <div class="card__person">
      <p class="person-name">Lena Hartwell</p>
      <p class="person-role">Relationship Director</p>
    </div>
    <div class="card__contact">
      <span class="phone">+34 600 482 937</span>
      <span class="email">lh@cedarharborhub.com</span>
    </div>
  </section>

  <section class="card card--back" aria-label="Business card back">
    <svg class="card__art" viewBox="0 0 800 444" aria-hidden="true">
      <rect width="800" height="444" fill="var(--brown)"/>
      <polygon points="800,0 222,396 390,396" fill="var(--brown-light)"/>
      <polygon points="800,0 390,396 574,396" fill="var(--olive)"/>
      <polygon points="800,0 574,396 800,396" fill="var(--brown)"/>
      <polygon points="86,396 800,396 800,444 0,444" fill="var(--olive)"/>
      <polygon points="0,396 86,396 0,444" fill="var(--brown-shade)"/>
    </svg>
    <div class="badge" aria-hidden="true"></div>
    <div class="brand-name">CEDAR HARBOR</div>
    <div class="card__url">cedarharborhub.com</div>
  </section>
</main>
</body>
</html>
```